Backdrop design that will flow throughout my Website

Name of my company is Maple Fern’s Mentoring

I would like you to provide designs of the Bee and drops of Honey...this will be

Target Market(s)

My targeted audiences are females, ages 40-55

Font styles to use
Script

Colors
6b449b
f37122
fbca95
e4daeb

Requirements
Must have
• Color concepts (orange, purple, and gray) with variations of brown for the Bee …see logo
Nice to have
• See sample FILE #6 below!! See the recessed flower in the background??

```html
<!DOCTYPE html>
<html lang="en">
<head>
<meta charset="utf-8">
<title>Maple Fern’s Mentoring – Website Backdrop</title>
<link href="https://fonts.googleapis.com/css2?family=Caveat+Brush&family=Catamaran:wght@500&display=swap" rel="stylesheet">
<style>
  :root {
    --stage: #2b2a29;
    --purple: #91288f;
    --white: #ffffff;
    --brown: #3d2412;
    --amber: #f0a21a;
    --honey-dark: #7a3a12;
    --honey-mid: #c8701c;
    --honey-light: #f3b33c;
  }
  * { margin: 0; padding: 0; box-sizing: border-box; }
  html, body {
    width: 1127px; height: 1200px; overflow: hidden;
    background: var(--stage);
  }
  .banner {
    position: absolute;
    left: 106px; width: 916px; height: 446px;
    overflow: hidden;
  }
  .banner--light { top: 96px; background: var(--white); }
  .banner--purple { top: 601px; background: var(--purple); }

  .banner__content {
    position: absolute; left: 0; top: 0;
    width: 500px; height: 100%;
    text-align: center;
  }
  .brand-name {
    position: absolute; left: 0; right: 0; top: 66px;
    font-family: "Catamaran", sans-serif; font-weight: 500;
    font-size: 30px; line-height: 1.1;
  }
  .tagline {
    position: absolute; left: 0; right: 0; top: 200px;
    font-family: "Caveat Brush", cursive;
    font-size: 40px; line-height: 58px;
    text-transform: uppercase; letter-spacing: 1px;
  }
  .owner {
    position: absolute; left: 0; right: 0; top: 370px;
    font-family: "Catamaran", sans-serif; font-weight: 500;
  }
  .owner__name { font-size: 21px; line-height: 24px; }
  .owner__role { font-size: 15px; line-height: 20px; }

  .banner--light .brand-name { color: var(--brown); }
  .banner--light .tagline { color: var(--purple); }
  .banner--light .owner { color: var(--brown); }
  .banner--purple .brand-name { color: var(--white); }
  .banner--purple .tagline { color: var(--amber); }
  .banner--purple .owner { color: var(--white); }

  .honey-photo {
    position: absolute; right: 0; top: 0;
    width: 424px; height: 100%;
    background:
      radial-gradient(ellipse 60% 35% at 70% 10%, var(--honey-dark), transparent 75%),
      radial-gradient(ellipse 80% 45% at 65% 85%, var(--honey-light), var(--honey-mid) 60%, transparent 90%),
      linear-gradient(180deg, rgba(122,58,18,0.35), rgba(243,179,60,0.55));
  }
</style>
</head>
<body>
  <section class="banner banner--light">
    <div class="banner__content">
      <p class="brand-name">Maple Fern’s Mentoring</p>
      <p class="tagline">Bees make honey.<br>Entrepreneurs make money</p>
      <div class="owner">
        <p class="owner__name">Carla Whitmore, MBA</p>
        <p class="owner__role">Serial Entrepreneur</p>
      </div>
    </div>
    <div class="honey-photo" role="img" aria-label="Photo of a honey dipper dripping honey into a glass jar, with a large faint bee motif behind it"></div>
  </section>

  <section class="banner banner--purple">
    <div class="banner__content">
      <p class="brand-name">Maple Fern’s Mentoring</p>
      <p class="tagline">Bees make honey.<br>Entrepreneurs make money</p>
      <div class="owner">
        <p class="owner__name">Carla Whitmore, MBA</p>
        <p class="owner__role">Serial Entrepreneur</p>
      </div>
    </div>
    <div class="honey-photo" role="img" aria-label="Photo of a honey dipper dripping honey into a glass jar, with a large faint bee motif behind it"></div>
  </section>
</body>
</html>
```